A online shop for solid wood need a Stationary design

A new online shop (in Austria and Germany) for solid wood and steel furniture (feldmark-tischwerk) needs a Stationay design (letterhead, business card, envelope etc...). Dining tables, coffee tables, TV furniture and similar furniture will be sold. Everything will be custom made.

```html
<!DOCTYPE html>
<html lang="en">
<head>
<meta charset="utf-8">
<title>Feldmark Tischwerk – Business Card</title>
<link href="https://fonts.googleapis.com/css2?family=Montserrat:wght@600;700&family=Roboto:wght@400;500&display=swap" rel="stylesheet">
<style>
  :root {
    --backdrop: #1b1b1b;
    --card: #141414;
    --card-edge: #d9212b;
    --accent: #e3252f;
    --text: #e9e9e9;
    --rule: #4a4a4a;
    --pattern-dark: #1c1c1c;
    --pattern-light: #3a3a3a;
  }
  * { margin: 0; padding: 0; box-sizing: border-box; }
  html, body {
    width: 1200px; height: 885px; overflow: hidden;
    background: var(--backdrop);
  }
  .canvas {
    position: relative; width: 1200px; height: 885px;
    display: flex; flex-direction: column; align-items: center; justify-content: center; gap: 48px;
  }
  .card {
    position: relative; width: 560px; height: 320px;
    background: var(--card);
    border: 2px solid var(--card-edge);
    border-radius: 3px;
    overflow: hidden;
    box-shadow: 0 18px 40px rgba(0,0,0,.55);
  }
  /* front */
  .brand {
    position: absolute; top: 44px; right: 42px;
    display: flex; align-items: center; gap: 10px;
    font-family: "Montserrat", sans-serif; font-weight: 700;
    font-size: 22px; letter-spacing: 2px; color: var(--accent);
    text-transform: uppercase;
  }
  .brand-square { width: 18px; height: 18px; background: var(--accent); }
  .person { position: absolute; left: 42px; top: 104px; }
  .person-name {
    font-family: "Montserrat", sans-serif; font-weight: 700;
    font-size: 20px; color: var(--accent); text-transform: uppercase; letter-spacing: .3px;
  }
  .person-role {
    font-family: "Montserrat", sans-serif; font-weight: 600;
    font-size: 16px; color: var(--text); margin-top: 2px;
  }
  .divider {
    position: absolute; left: 42px; right: 42px; top: 170px; height: 1px;
    background: linear-gradient(90deg, transparent, var(--rule) 15%, #8a8a8a 60%, var(--rule) 85%, transparent);
  }
  .contacts {
    position: absolute; left: 42px; top: 190px; list-style: none;
    font-family: "Roboto", sans-serif; font-size: 15px; color: var(--text);
  }
  .contacts li { display: flex; align-items: center; gap: 9px; height: 26px; }
  .contacts svg { width: 15px; height: 15px; fill: var(--accent); flex: none; }
  .address {
    position: absolute; right: 42px; top: 190px; text-align: right;
    font-family: "Roboto", sans-serif; font-size: 15px; line-height: 26px; color: var(--text);
  }
  /* back */
  .pattern-field {
    position: absolute; inset: 0;
    background: linear-gradient(120deg, var(--pattern-light) 0%, var(--pattern-dark) 55%, #262626 100%);
  }
  .back-brand {
    position: absolute; right: 40px; top: 40px;
    font-family: "Montserrat", sans-serif; font-weight: 700;
    font-size: 18px; letter-spacing: 2px; color: #f4f4f4; text-transform: uppercase;
  }
</style>
</head>
<body>
<main class="canvas">
  <section class="card card-front">
    <div class="brand"><span class="brand-square"></span>Feldmark Tischwerk</div>

    <div class="person">
      <p class="person-name">Jonas Weidinger</p>
      <p class="person-role">Managing Director</p>
    </div>

    <div class="divider"></div>

    <ul class="contacts">
      <li>
        <svg viewBox="0 0 24 24" aria-hidden="true"><path d="M6.6 10.8c1.4 2.8 3.8 5.1 6.6 6.6l2.2-2.2c.3-.3.7-.4 1-.2 1.1.4 2.3.6 3.6.6.6 0 1 .4 1 1V20c0 .6-.4 1-1 1C10.6 21 3 13.4 3 4c0-.6.4-1 1-1h3.5c.6 0 1 .4 1 1 0 1.3.2 2.5.6 3.6.1.3 0 .7-.2 1l-2.3 2.2z"/></svg>
        +43 660 2184730
      </li>
      <li>
        <svg viewBox="0 0 24 24" aria-hidden="true"><path d="M2 5h20v14H2z M3.5 6.5l8.5 6.5 8.5-6.5" stroke="#141414" stroke-width="1.6"/></svg>
        info@feldmarktischwerk.com
      </li>
      <li>
        <svg viewBox="0 0 24 24" aria-hidden="true"><circle cx="12" cy="12" r="10"/><path d="M2 12h20M12 2c3 3 3 17 0 20M12 2c-3 3-3 17 0 20" stroke="#141414" stroke-width="1.5" fill="none"/></svg>
        www.feldmarktischwerk.com
      </li>
    </ul>

    <address class="address" style="font-style:normal">
      Feldmark Tischwerk, LLC<br>
      14 Lindenweg<br>
      4020 Linz, Austria
    </address>
  </section>

  <section class="card card-back">
    <div class="pattern-field" role="img" aria-label="Embossed repeating brand pattern in dark grey tones"></div>
    <div class="back-brand">Feldmark Tischwerk</div>
  </section>
</main>
</body>
</html>
```